Brell & Partners Property Management

I want 4 different cards so that i can mail to my farm once per quarter. I want to go back to a 5X8 card or smaller. I am attaching an example of what we did in the past. I would like the new cards start with the following:
1. Tired of dealing with tenant problems at 6:00 on a Friday Night?
2. Would you like to take you next vacation worry free?
3. Are your tenants paying below market rents?
4. Do your tenant leases fully protect you?
I would like to have one of these "hooks" to lead off each card with a brief explanation of the services we provide. Back of the card can be similar to the one I attached.

Target Market(s)

Income Property Owners that might be in need of a property management company.

Font styles to use
Serif

Requirements
Must have
• 4 separate cards that i can email out each quarter.
• Each card must have a "hook" or "call to action"
Nice to have
• Less verbiage and some catchy graphics or photo
• If you have an idea for catchier calls to action, feel free to submit.
Should not have
• Too many words. The postcard I uploaded has way too much verbiage.

```html
<!DOCTYPE html>
<html lang="en">
<head>
<meta charset="utf-8">
<title>Brell &amp; Partners Property Management – Quarterly Postcards</title>
<link rel="stylesheet" href="https://fonts.googleapis.com/css2?family=Open+Sans:wght@300;400;600;700&family=Open+Sans+Condensed:wght@700&display=swap">
<style>
  :root{
    --page:#e9e9e9;
    --card:#ffffff;
    --charcoal:#4a4a4c;
    --ink:#2f2f31;
    --gold:#b4955e;
    --gold-light:#cdb68c;
    --text-light:#ffffff;
    --text-soft:#e4e4e4;
    --line:#c9c9c9;
    --photo-a:#c9cdd2;
    --photo-b:#5a6070;
  }
  *{box-sizing:border-box;margin:0;padding:0}
  html,body{width:1200px;height:979px;overflow:hidden}
  body{background:var(--page);font-family:"Open Sans",Arial,sans-serif;position:relative;color:var(--ink)}

  .postcard{position:absolute;width:480px;height:300px;background:var(--card);overflow:hidden;box-shadow:0 2px 6px rgba(0,0,0,.12)}
  .postcard--q1{left:105px;top:24px}
  .postcard--q2{left:615px;top:24px}
  .postcard--q3{left:105px;top:346px}
  .postcard--q4{left:615px;top:346px}
  .postcard--back{left:360px;top:668px}

  .card-art{position:absolute;left:0;top:0}

  .brand{position:absolute;left:20px;top:14px}
  .brand__name{font-weight:300;font-size:22px;line-height:23px;color:var(--ink);letter-spacing:.3px;text-transform:uppercase}
  .brand__tagline{margin-top:6px;font-size:7.5px;letter-spacing:1.2px;color:var(--ink);font-weight:600}

  .hook{position:absolute;left:16px;top:102px;width:222px}
  .hook__question{display:flex;gap:7px;color:var(--text-light);font-size:13px;line-height:17px;font-weight:600}
  .hook__question svg{flex:0 0 13px;margin-top:2px}
  .hook__services{margin:8px 0 0 20px;color:var(--text-soft);font-size:9.5px;line-height:13.5px}

  .cta__title{position:absolute;left:17px;font-family:"Open Sans Condensed","Arial Narrow",sans-serif;font-weight:700;font-size:14px;color:var(--ink);letter-spacing:.2px}
  .cta__phone{position:absolute;left:0;height:26px;background:var(--gold);color:var(--text-light);display:flex;align-items:center;gap:7px;padding-left:15px;font-size:18px;font-weight:600;letter-spacing:1px;clip-path:polygon(0 0,100% 0,95% 100%,0 100%)}
  .cta__url{position:absolute;left:17px;font-size:9.5px;color:var(--ink)}

  .front .cta__title{top:227px}
  .front .cta__phone{top:248px;width:218px}
  .front .cta__url{top:279px}

  .testimonial{position:absolute;left:18px;top:88px;width:265px;color:var(--text-light);font-size:9.5px;line-height:13px}
  .testimonial__mark{font-size:24px;line-height:10px;font-weight:700;vertical-align:-8px;margin-right:3px}
  .back .cta__title{top:207px;color:var(--text-light)}
  .back .cta__phone{top:229px;width:222px}
  .back .cta__url{top:265px;color:var(--text-light)}
  .address-lines{position:absolute;left:318px;top:48px;width:140px}
  .address-lines span{display:block;height:1px;background:var(--line);margin-bottom:26px}
</style>
</head>
<body>

<!-- Reusable front artwork: band, gold chevron, photo area -->
<svg width="0" height="0" style="position:absolute" aria-hidden="true">
  <defs>
    <linearGradient id="photoTone" x1="0" y1="0" x2="1" y2="1">
      <stop offset="0" stop-color="#c9cdd2"/>
      <stop offset="1" stop-color="#5a6070"/>
    </linearGradient>
    <symbol id="tick" viewBox="0 0 16 16"><circle cx="8" cy="8" r="7" fill="none" stroke="#b4955e" stroke-width="1.4"/><path d="M4.5 8.2l2.4 2.4 4.6-5" fill="none" stroke="#b4955e" stroke-width="1.6"/></symbol>
    <symbol id="phone" viewBox="0 0 22 22"><circle cx="11" cy="11" r="10" fill="none" stroke="#fff" stroke-width="1.6"/><path d="M7.5 6.5c.6-.6 1.3-.5 1.7.1l.8 1.3c.3.5.2 1-.2 1.4l-.5.5c.6 1.3 1.6 2.3 2.9 2.9l.5-.5c.4-.4.9-.5 1.4-.2l1.3.8c.6.4.7 1.1.1 1.7-1 1-2.4 1.2-4 .3-1.7-1-3.1-2.4-4.1-4.1-.9-1.6-.7-3 .1-4.2z" fill="#fff"/></symbol>
  </defs>
</svg>

<section class="postcard postcard--q1 front" aria-label="Quarter 1 postcard front">
  <svg class="card-art" width="480" height="300" viewBox="0 0 480 300">
    <polygon points="0,93 256,93 233,172 252,221 0,221" fill="var(--charcoal)"/>
    <polygon points="285,0 303,0 256,172 310,300 292,300 238,172" fill="var(--gold-light)"/>
    <polygon role="img" aria-label="Photo: smiling property manager in a suit holding out house keys and a small model house" points="312,0 480,0 480,300 320,300 267,172" fill="url(#photoTone)"/>
  </svg>
  <div class="brand"><div class="brand__name">Brell &amp;<br>Partners</div><div class="brand__tagline">PROPERTY MANAGEMENT</div></div>
  <div class="hook">
    <p class="hook__question"><svg width="13" height="13"><use href="#tick"/></svg>Tired of dealing with tenant problems at 6:00 on a Friday Night?</p>
    <p class="hook__services">We answer the late calls, handle repairs and deal with tenants, so your weekends stay yours.</p>
  </div>
  <div class="cta__title">CALL TODAY FOR YOUR FREE QUOTE</div>
  <div class="cta__phone"><svg width="16" height="16"><use href="#phone"/></svg>208-555-0147</div>
  <div class="cta__url">brellpartnersproperty.com</div>
</section>

<section class="postcard postcard--q2 front" aria-label="Quarter 2 postcard front">
  <svg class="card-art" width="480" height="300" viewBox="0 0 480 300">
    <polygon points="0,93 256,93 233,172 252,221 0,221" fill="var(--charcoal)"/>
    <polygon points="285,0 303,0 256,172 310,300 292,300 238,172" fill="var(--gold-light)"/>
    <polygon role="img" aria-label="Photo: relaxed property owner on holiday while the manager looks after the home" points="312,0 480,0 480,300 320,300 267,172" fill="url(#photoTone)"/>
  </svg>
  <div class="brand"><div class="brand__name">Brell &amp;<br>Partners</div><div class="brand__tagline">PROPERTY MANAGEMENT</div></div>
  <div class="hook">
    <p class="hook__question"><svg width="13" height="13"><use href="#tick"/></svg>Would you like to take you next vacation worry free?</p>
    <p class="hook__services">We collect rent, inspect homes and manage maintenance while you are away, with clear monthly reports.</p>
  </div>
  <div class="cta__title">CALL TODAY FOR YOUR FREE QUOTE</div>
  <div class="cta__phone"><svg width="16" height="16"><use href="#phone"/></svg>208-555-0147</div>
  <div class="cta__url">brellpartnersproperty.com</div>
</section>

<section class="postcard postcard--q3 front" aria-label="Quarter 3 postcard front">
  <svg class="card-art" width="480" height="300" viewBox="0 0 480 300">
    <polygon points="0,93 256,93 233,172 252,221 0,221" fill="var(--charcoal)"/>
    <polygon points="285,0 303,0 256,172 310,300 292,300 238,172" fill="var(--gold-light)"/>
    <polygon role="img" aria-label="Photo: rental house exterior with a for rent sign" points="312,0 480,0 480,300 320,300 267,172" fill="url(#photoTone)"/>
  </svg>
  <div class="brand"><div class="brand__name">Brell &amp;<br>Partners</div><div class="brand__tagline">PROPERTY MANAGEMENT</div></div>
  <div class="hook">
    <p class="hook__question"><svg width="13" height="13"><use href="#tick"/></svg>Are your tenants paying below market rents?</p>
    <p class="hook__services">We study local rents, set the right price and fill vacancies fast with well-screened tenants.</p>
  </div>
  <div class="cta__title">CALL TODAY FOR YOUR FREE QUOTE</div>
  <div class="cta__phone"><svg width="16" height="16"><use href="#phone"/></svg>208-555-0147</div>
  <div class="cta__url">brellpartnersproperty.com</div>
</section>

<section class="postcard postcard--q4 front" aria-label="Quarter 4 postcard front">
  <svg class="card-art" width="480" height="300" viewBox="0 0 480 300">
    <polygon points="0,93 256,93 233,172 252,221 0,221" fill="var(--charcoal)"/>
    <polygon points="285,0 303,0 256,172 310,300 292,300 238,172" fill="var(--gold-light)"/>
    <polygon role="img" aria-label="Photo: hands signing a lease agreement at a desk" points="312,0 480,0 480,300 320,300 267,172" fill="url(#photoTone)"/>
  </svg>
  <div class="brand"><div class="brand__name">Brell &amp;<br>Partners</div><div class="brand__tagline">PROPERTY MANAGEMENT</div></div>
  <div class="hook">
    <p class="hook__question"><svg width="13" height="13"><use href="#tick"/></svg>Do your tenant leases fully protect you?</p>
    <p class="hook__services">Our up-to-date leases, move-in records and legal know-how keep your property and income safe.</p>
  </div>
  <div class="cta__title">CALL TODAY FOR YOUR FREE QUOTE</div>
  <div class="cta__phone"><svg width="16" height="16"><use href="#phone"/></svg>208-555-0147</div>
  <div class="cta__url">brellpartnersproperty.com</div>
</section>

<section class="postcard postcard--back back" aria-label="Postcard back, shared by all four cards">
  <svg class="card-art" width="480" height="300" viewBox="0 0 480 300">
    <rect x="0" y="0" width="300" height="79" fill="#f4f4f4"/>
    <polygon points="0,79 294,79 308,199 0,199" fill="var(--gold)"/>
    <polygon points="0,199 308,199 328,300 0,300" fill="var(--charcoal)"/>
  </svg>
  <div class="brand"><div class="brand__name">Brell &amp;<br>Partners</div><div class="brand__tagline">PROPERTY MANAGEMENT</div></div>
  <p class="testimonial"><span class="testimonial__mark">“</span>We have trusted Brell &amp; Partners with our rentals for years. Calls and repairs are handled quickly, rents arrive on time and reports are always clear. We gladly recommend the team to any owner who wants steady, caring management.<br>– Marion K.</p>
  <div class="cta__title">CALL TODAY FOR YOUR FREE QUOTE</div>
  <div class="cta__phone"><svg width="16" height="16"><use href="#phone"/></svg>208-555-0147</div>
  <div class="cta__url">brellpartnersproperty.com</div>
  <div class="address-lines" aria-hidden="true"><span></span><span></span><span></span><span></span></div>
</section>

</body>
</html>
```